Harbor Key Realty - New Agent Opportunity Overview

We want to create a one (1) page brochure to highlight what Harbor Key Realty (a real estate brokerage) offers new agents. I have uploaded a Word doc that has all the text we want on the flyer. We want a professional looking design.
Industry/Entity Type
Real Estate Agent
Colors
3176b5
33a6d7

```html
<!DOCTYPE html>
<html lang="en">
<head>
<meta charset="utf-8">
<title>Harbor Key Realty – New Agent Opportunity</title>
<link href="https://fonts.googleapis.com/css2?family=Open+Sans:wght@300;400;600;700;800&display=swap" rel="stylesheet">
<style>
:root{
  --navy:#1f2433;
  --indigo:#3a3d91;
  --ink:#555557;
  --text:#68686b;
  --row-gray:#dcdddd;
  --row-indigo:#d3d4ec;
  --page:#ececec;
  --white:#ffffff;
}
*{margin:0;padding:0;box-sizing:border-box}
html,body{width:1200px;height:1200px;overflow:hidden;background:var(--page);font-family:'Open Sans',sans-serif}
.stage{position:relative;width:1200px;height:1200px}
.flyer{position:absolute;left:136px;top:0;width:1187px;height:1536px;background:var(--white);transform:scale(0.78125);transform-origin:0 0;overflow:hidden}
.header{position:absolute;left:0;top:0;width:1187px;height:134px;background:var(--navy)}
.brand{position:absolute;left:55px;top:27px;width:392px;height:76px;border:4px solid var(--indigo);display:flex;align-items:center;justify-content:center}
.brand-name{color:var(--white);font-weight:700;font-size:30px;letter-spacing:5px}
.announce{position:absolute;left:545px;top:14px;width:642px;height:86px}
.announce svg{position:absolute;left:0;top:0}
.announce-text{position:absolute;right:54px;top:10px;text-align:right;color:var(--white);font-size:27px;line-height:32px}
.announce-text strong{font-weight:800;font-size:31px;display:block}
.photo{position:absolute;left:560px;top:100px;width:627px;height:397px;background:linear-gradient(90deg,#ffffff 0%,#dfe9ef 30%,#c9d6df 60%,#aebdc9 100%)}
.headline{position:absolute;left:58px;top:172px;color:var(--ink);line-height:1}
.headline .light{font-weight:400;font-size:36px}
.headline .big{font-weight:800;font-size:61px;line-height:62px;display:block}
.headline .accent{color:var(--indigo)}
.headline .dash{font-weight:400;font-size:30px}
.rule-left{position:absolute;left:0;top:497px;width:593px;height:6px;background:var(--indigo)}
.rule-right{position:absolute;left:593px;top:497px;width:594px;height:6px;background:var(--navy)}
.divider{position:absolute;left:587px;width:3px;background:linear-gradient(180deg,transparent,#b8b8bc 20%,#b8b8bc 80%,transparent)}
.icon{position:absolute;width:72px;height:72px;border-radius:50%;background:var(--indigo);display:flex;align-items:center;justify-content:center}
.sec-title{position:absolute;font-weight:700;font-size:31px;line-height:32px;color:var(--ink)}
.sec-title .accent{color:var(--indigo)}
.list{position:absolute;list-style:none;color:var(--text);font-size:20px;line-height:24px}
.list li{position:relative;padding-left:42px}
.list li svg{position:absolute;left:0;top:4px}
.deal-table{position:absolute;left:55px;top:954px;width:1076px;border-collapse:separate;border-spacing:5px 0;margin-left:-5px;text-align:center;font-size:20px;color:var(--ink)}
.deal-table th{height:45px;color:var(--white);font-weight:700;font-size:23px}
.deal-table th.type{background:var(--navy)}
.deal-table th.split{background:var(--indigo)}
.deal-table td{height:40px;font-weight:400}
.deal-table td.split{font-weight:600}
.deal-table tr.shaded td.type{background:var(--row-gray)}
.deal-table tr.shaded td.split{background:var(--row-indigo)}
.table-shadow{position:absolute;left:80px;top:1118px;width:1030px;height:26px;background:radial-gradient(ellipse at top,rgba(60,60,110,.25),transparent 70%)}
.footer{position:absolute;left:0;top:1460px;width:1187px;height:76px;background:var(--navy);color:var(--white);display:flex;align-items:center}
.footer .phone{position:absolute;left:58px;font-weight:700;font-size:35px}
.footer .web,.footer .mail{position:absolute;font-size:23px;font-weight:300}
.footer .web{left:412px}
.footer .mail{right:54px}
.footer b{font-weight:700}
.footer .sep{position:absolute;top:8px;width:3px;height:60px;background:var(--indigo)}
</style>
</head>
<body>
<div class="stage">
<div class="flyer">

  <header class="header">
    <div class="brand"><span class="brand-name">HARBOR KEY REALTY</span></div>
  </header>

  <div class="photo" role="img" aria-label="Photo of an agent in shirt and tie holding out a small model house with keys"></div>

  <div class="announce">
    <svg width="642" height="86"><polygon points="38,0 642,0 642,86 0,86" fill="#3a3d91"/></svg>
    <div class="announce-text">HKR HOME CENTER BROOKHAVEN,<strong>MARYLAND IS NOW OPEN!</strong></div>
  </div>

  <h1 class="headline">
    <span class="light">IGNITE YOUR</span>
    <span class="big">REAL ESTATE</span>
    <span class="big">BUSINESS <span class="dash">–</span></span>
    <span class="big"><span class="light">JOIN</span> <span class="accent">HARBOR KEY</span></span>
    <span class="big accent">REALTY</span>
  </h1>

  <div class="rule-left"></div>
  <div class="rule-right"></div>

  <div class="divider" style="top:530px;height:400px"></div>
  <div class="divider" style="top:1165px;height:270px"></div>

  <!-- Consumer direct -->
  <div class="icon" style="left:55px;top:538px">
    <svg width="40" height="40" viewBox="0 0 40 40" fill="none" stroke="#fff" stroke-width="2.2" stroke-linejoin="round"><rect x="5" y="18" width="7" height="16"/><path d="M12 20l7-10c2-2 4-1 4 1l-1 6h9c2 0 3 2 2 4l-3 10c-1 2-2 3-4 3H12"/></svg>
  </div>
  <h2 class="sec-title" style="left:155px;top:540px"><span class="accent">CONSUMER DIRECT</span><br>ADVANTAGE</h2>
  <ul class="list" style="left:155px;top:626px">
    <li style="margin-bottom:13px"><svg width="22" height="18"><polyline points="2,9 8,15 20,3" fill="none" stroke="#3a3d91" stroke-width="3"/></svg>Lender Referrals</li>
    <li style="margin-bottom:13px"><svg width="22" height="18"><polyline points="2,9 8,15 20,3" fill="none" stroke="#3a3d91" stroke-width="3"/></svg>HomeFind Leads</li>
    <li><svg width="22" height="18"><polyline points="2,9 8,15 20,3" fill="none" stroke="#3a3d91" stroke-width="3"/></svg>NestList.com /<br>OpenDoorsNearby.com</li>
  </ul>
  <ul class="list" style="left:662px;top:540px">
    <li style="margin-bottom:17px"><svg width="22" height="18"><polyline points="2,9 8,15 20,3" fill="none" stroke="#3a3d91" stroke-width="3"/></svg>Credit Trigger Campaigns</li>
    <li style="margin-bottom:17px"><svg width="22" height="18"><polyline points="2,9 8,15 20,3" fill="none" stroke="#3a3d91" stroke-width="3"/></svg>Consumer Behavior Campaigns</li>
    <li style="margin-bottom:17px"><svg width="22" height="18"><polyline points="2,9 8,15 20,3" fill="none" stroke="#3a3d91" stroke-width="3"/></svg>HKR Call Center Marketing Team</li>
    <li style="margin-bottom:17px"><svg width="22" height="18"><polyline points="2,9 8,15 20,3" fill="none" stroke="#3a3d91" stroke-width="3"/></svg>HKR Sponsored Local Events</li>
    <li><svg width="22" height="18"><polyline points="2,9 8,15 20,3" fill="none" stroke="#3a3d91" stroke-width="3"/></svg>Shared Lender Leads</li>
  </ul>

  <!-- Compensation -->
  <div class="icon" style="left:59px;top:796px">
    <svg width="42" height="40" viewBox="0 0 42 40" fill="none" stroke="#fff" stroke-width="2"><circle cx="9" cy="30" r="6"/><circle cx="21" cy="30" r="6"/><circle cx="33" cy="30" r="6"/><polyline points="4,18 14,10 22,14 36,4"/><polyline points="30,4 36,4 36,10"/></svg>
  </div>
  <h2 class="sec-title" style="left:159px;top:798px"><span class="accent">MAXIMIZED</span><br>COMPENSATION</h2>
  <ul class="list" style="left:159px;top:884px">
    <li><svg width="22" height="18"><polyline points="2,9 8,15 20,3" fill="none" stroke="#3a3d91" stroke-width="3"/></svg>No desk fees. No royalty fees. No<br>franchise fees.</li>
  </ul>
  <ul class="list" style="left:662px;top:800px">
    <li style="margin-bottom:17px"><svg width="22" height="18"><polyline points="2,9 8,15 20,3" fill="none" stroke="#3a3d91" stroke-width="3"/></svg>Company paid E&amp;O</li>
    <li><svg width="22" height="18"><polyline points="2,9 8,15 20,3" fill="none" stroke="#3a3d91" stroke-width="3"/></svg>Transaction fee of $550 includes<br>Transaction Coordinator</li>
  </ul>

  <table class="deal-table">
    <thead><tr><th class="type">TYPE OF DEAL</th><th class="split">COMMISSION SPLIT</th></tr></thead>
    <tbody>
      <tr><td class="type">SELF-GENERATED</td><td class="split">90% / 10%</td></tr>
      <tr class="shaded"><td class="type">LENDER REFERRED LEADS</td><td class="split">70% / 30%</td></tr>
      <tr><td class="type">HKR GENERATED LEADS / REFERRALS</td><td class="split">55% / 45%</td></tr>
    </tbody>
  </table>
  <div class="table-shadow"></div>

  <!-- Support -->
  <div class="icon" style="left:59px;top:1186px">
    <svg width="42" height="42" viewBox="0 0 42 42" fill="none" stroke="#fff" stroke-width="2.2" stroke-linejoin="round"><path d="M4 26l10-10 6 4 6-4 12 10-10 10-8-6-6 6z"/><path d="M14 16l8 8"/><path d="M21 2v5M11 5l3 4M31 5l-3 4"/></svg>
  </div>
  <h2 class="sec-title" style="left:159px;top:1190px">COMPLETE SUPPORT<br>SYSTEM</h2>
  <ul class="list" style="left:159px;top:1275px">
    <li style="margin-bottom:10px"><svg width="22" height="18"><polyline points="2,9 8,15 20,3" fill="none" stroke="#3a3d91" stroke-width="3"/></svg>Powerful Suite of Cloud Based Tools</li>
    <li style="margin-bottom:10px"><svg width="22" height="18"><polyline points="2,9 8,15 20,3" fill="none" stroke="#3a3d91" stroke-width="3"/></svg>IDX, CRM and Transaction Management</li>
    <li style="margin-bottom:10px"><svg width="22" height="18"><polyline points="2,9 8,15 20,3" fill="none" stroke="#3a3d91" stroke-width="3"/></svg>HKR Call Center Support for<br>Leads and Deals</li>
    <li><svg width="22" height="18"><polyline points="2,9 8,15 20,3" fill="none" stroke="#3a3d91" stroke-width="3"/></svg>Transaction Coordinator</li>
  </ul>
  <ul class="list" style="left:662px;top:1190px">
    <li style="margin-bottom:10px"><svg width="22" height="18"><polyline points="2,9 8,15 20,3" fill="none" stroke="#3a3d91" stroke-width="3"/></svg>Virtual Assistants Available</li>
    <li style="margin-bottom:13px"><svg width="22" height="18"><polyline points="2,9 8,15 20,3" fill="none" stroke="#3a3d91" stroke-width="3"/></svg>24/7 Workspace Access</li>
    <li style="margin-bottom:13px"><svg width="22" height="18"><polyline points="2,9 8,15 20,3" fill="none" stroke="#3a3d91" stroke-width="3"/></svg>Coaching / Mentoring</li>
    <li style="margin-bottom:13px"><svg width="22" height="18"><polyline points="2,9 8,15 20,3" fill="none" stroke="#3a3d91" stroke-width="3"/></svg>Social Media / Marketing Expertise</li>
    <li><svg width="22" height="18"><polyline points="2,9 8,15 20,3" fill="none" stroke="#3a3d91" stroke-width="3"/></svg>Nationwide Partnerships with<br>Top Lenders</li>
  </ul>

  <footer class="footer">
    <span class="phone">(555) 014-2290</span>
    <span class="sep" style="left:365px"></span>
    <span class="web">www.<b>harborkeyusa</b>.com</span>
    <span class="sep" style="left:748px"></span>
    <span class="mail">support@<b>harborkeyusa</b>.com</span>
  </footer>

</div>
</div>
</body>
</html>
```